i need a template design for online store

hi great designers, i need a template for any online store. But preferably well owned shopping carts. I would be an added advantage if the store is setup for me. I need a mature and attractive colours. My online store deals in electronics.

Shopping

1 page

```html
<!DOCTYPE html>
<html lang="en">
<head>
<meta charset="utf-8">
<title>Kenvo Electronics – Store</title>
<link rel="stylesheet" href="https://fonts.googleapis.com/css2?family=Open+Sans:wght@300;400;600;700&display=swap">
<style>
:root{
  --navy:#0b2a6b;
  --blue-deep:#123f98;
  --blue:#1f63c9;
  --blue-light:#3f8ae6;
  --nav-top:#5aa2f0;
  --nav-bottom:#2f7fdc;
  --page:#f1f3f6;
  --white:#ffffff;
  --line:#dde1e7;
  --ink:#2b2f36;
  --muted:#8a9099;
  --orange:#f08a1c;
  --yellow:#f7c21b;
  --footer:#0a1f4c;
  --footer-bar:#071738;
  --footer-text:#9fb0d0;
}
*{margin:0;padding:0;box-sizing:border-box}
html,body{width:805px;height:1200px;overflow:hidden}
body{font-family:"Open Sans",Arial,sans-serif;color:var(--ink);
  background:linear-gradient(180deg,var(--navy) 0,var(--blue-deep) 90px,var(--blue) 220px,#a9c6ef 380px,var(--page) 440px,var(--page) 100%);
  position:relative}
.wrap{position:absolute;left:126px;width:552px}

/* header */
.site-header{top:0;height:78px}
.utility{position:absolute;right:0;top:7px;display:flex;gap:6px;font-size:6px;color:#cfdcf5;letter-spacing:.3px}
.utility span+span::before{content:"|";margin-right:6px;color:#6d8ccc}
.brand{position:absolute;left:0;top:28px;font-size:19px;font-weight:300;color:var(--white);letter-spacing:.2px}
.cart{position:absolute;right:0;top:34px;display:flex;align-items:center;gap:6px;color:var(--white);font-size:7px;line-height:1.25}
.cart svg{display:block}

/* nav */
.main-nav{top:78px;height:20px;background:linear-gradient(180deg,var(--nav-top),var(--nav-bottom));display:flex;border-radius:2px 2px 0 0}
.main-nav a{flex:1;text-align:center;font-size:6.5px;font-weight:600;color:var(--white);line-height:20px;text-decoration:none;border-right:1px solid rgba(255,255,255,.25);letter-spacing:.3px}
.main-nav a:last-child{border-right:0}
.main-nav a.active{background:rgba(255,255,255,.18)}

/* hero */
.hero{top:102px;height:242px;background:linear-gradient(180deg,#ffffff,#eef1f5);}
.hero-kicker{position:absolute;left:20px;top:50px;font-size:14px;color:var(--ink)}
.hero-title{position:absolute;left:20px;top:74px;font-size:23px;font-weight:400;color:var(--ink)}
.hero-text{position:absolute;left:20px;top:110px;width:190px;font-size:5.5px;line-height:1.6;color:var(--muted)}
.btn-buy{position:absolute;left:20px;top:152px;background:var(--yellow);color:var(--ink);font-size:6px;font-weight:700;padding:5px 10px;letter-spacing:.3px}
.hero-media{position:absolute;left:225px;top:20px;width:310px;height:190px;border-radius:40px;
  background:radial-gradient(ellipse at 55% 55%,#5b6068 0,#2b2e33 45%,rgba(220,224,230,0) 72%)}
.dots{position:absolute;left:0;right:0;bottom:14px;display:flex;justify-content:center;gap:4px}
.dots i{width:5px;height:5px;border-radius:50%;background:#b9bec6}
.dots i.on{background:#4a4f57}

/* features */
.features{top:356px;height:74px;display:flex;gap:8px}
.feature{flex:1;background:var(--white);border:1px solid var(--line);position:relative}
.feature-media{position:absolute;left:8px;top:10px;width:58px;height:54px;border-radius:4px}
.feature h3{position:absolute;left:72px;top:10px;font-size:10px;font-weight:400;color:var(--ink)}
.feature p{position:absolute;left:72px;top:27px;width:100px;font-size:5.5px;line-height:1.5;color:var(--muted)}
.btn-view{position:absolute;left:72px;top:50px;background:var(--blue);color:var(--white);font-size:5px;font-weight:700;padding:3px 7px}

/* products */
.section-title{height:16px;display:flex;align-items:center;gap:12px;font-size:9px;letter-spacing:.6px;color:var(--ink)}
.section-title::before,.section-title::after{content:"";flex:1;height:1px;background:#c9ced6}
.section-title.accent{color:var(--orange)}
.section-title.accent::before,.section-title.accent::after{background:#f3c48f}
.latest-title{top:496px}
.best-title{top:742px}
.grid{display:flex;gap:12px}
.latest-grid{top:528px}
.best-grid{top:773px}
.product{width:129px;height:168px;background:var(--white);border:1px solid var(--line);position:relative}
.product-media{position:absolute;left:10px;top:8px;width:107px;height:84px;border-radius:6px}
.product h4{position:absolute;left:8px;top:100px;font-size:7.5px;font-weight:600;color:var(--ink)}
.product h4.hot{color:var(--orange)}
.product p{position:absolute;left:8px;top:112px;width:112px;font-size:5px;color:var(--muted)}
.price-bar{position:absolute;left:0;right:0;bottom:0;height:34px;border-top:1px solid var(--line);display:flex}
.price{flex:1;font-size:9px;font-weight:600;line-height:34px;padding-left:8px;color:var(--ink)}
.add-cart{width:48px;background:#eceef1;display:flex;align-items:center;justify-content:center;border-left:1px solid var(--line)}

/* footer */
.site-footer{position:absolute;left:0;top:992px;width:805px;height:208px;background:var(--footer);color:var(--footer-text)}
.footer-cols{position:absolute;left:126px;top:28px;width:552px;display:flex}
.footer-col h5{font-size:7px;font-weight:700;color:var(--white);letter-spacing:.4px;margin-bottom:6px}
.footer-col li{list-style:none;font-size:5.5px;line-height:1.75}
.newsletter{width:170px}
.newsletter p{font-size:5.5px;margin-bottom:6px}
.news-input{width:100px;height:11px;background:var(--white);border-radius:1px;margin-bottom:5px}
.btn-subscribe{display:inline-block;background:var(--orange);color:var(--white);font-size:5px;font-weight:700;padding:3px 7px;margin-bottom:6px}
.pay-row{display:flex;gap:3px}
.pay-row i{width:17px;height:10px;background:#d9dfe9;border-radius:1px}
.link-col{width:96px}
.footer-bar{position:absolute;left:0;bottom:0;width:805px;height:34px;background:var(--footer-bar)}
.copyright{position:absolute;left:126px;top:13px;font-size:5.5px}
.social{position:absolute;right:127px;top:11px;display:flex;gap:4px}
.social i{width:11px;height:11px;background:#c7d3ea;border-radius:1px}
</style>
</head>
<body>

<header class="wrap site-header">
  <div class="utility"><span>SIGN IN</span><span>LOGIN</span><span>MY ACCOUNT</span><span>SUPPORT</span></div>
  <div class="brand">Kenvo Electronics</div>
  <div class="cart">
    <svg width="16" height="14" viewBox="0 0 16 14" aria-hidden="true"><path d="M1 1h2.5l2 8h8l1.5-6H4.2" fill="none" stroke="#fff" stroke-width="1.3"/><circle cx="6.5" cy="12" r="1.2" fill="#fff"/><circle cx="12.5" cy="12" r="1.2" fill="#fff"/></svg>
    <div>My Cart<br>0 Items</div>
  </div>
</header>

<nav class="wrap main-nav">
  <a class="active">HOME</a><a>ABOUT US</a><a>PRODUCTS</a><a>BEST SELLING</a><a>RESOURCES</a><a>SUPPORT</a><a>CONTACT</a>
</nav>

<section class="wrap hero">
  <div class="hero-kicker">Electronic Products</div>
  <h1 class="hero-title">Praesent metus psum</h1>
  <p class="hero-text">Suspendisse dictum tellus vel lorem pulvinar, in sagittis purus finibus. Nulla facilisi sed quis elit.</p>
  <span class="btn-buy">BUY NOW</span>
  <div class="hero-media" role="img" aria-label="Product photo of three smart watches"></div>
  <div class="dots"><i class="on"></i><i></i><i></i><i></i></div>
</section>

<section class="wrap features">
  <div class="feature">
    <div class="feature-media" role="img" aria-label="Photo of headphones" style="background:linear-gradient(135deg,#d9dce1,#3a3d42)"></div>
    <h3>Why Choose Us</h3>
    <p>Quality gadgets with fast free delivery.</p>
    <span class="btn-view">VIEW ALL</span>
  </div>
  <div class="feature">
    <div class="feature-media" role="img" aria-label="Photo of a steam iron" style="background:linear-gradient(135deg,#dfe6f2,#4f6fb0)"></div>
    <h3>Best Deals</h3>
    <p>Weekly savings on top brand devices.</p>
    <span class="btn-view">VIEW ALL</span>
  </div>
  <div class="feature">
    <div class="feature-media" role="img" aria-label="Photo of a portable radio" style="background:linear-gradient(135deg,#e2e4e7,#55595f)"></div>
    <h3>New Arrivals</h3>
    <p>Fresh tech arriving every single week.</p>
    <span class="btn-view">VIEW ALL</span>
  </div>
</section>

<h2 class="wrap section-title latest-title">LATEST PRODUCTS</h2>
<section class="wrap grid latest-grid">
  <article class="product"><div class="product-media" role="img" aria-label="Photo of a car power inverter" style="background:linear-gradient(135deg,#eceef1,#2f3237)"></div><h4 class="hot">Product Name</h4><p>Short item description goes right here</p><div class="price-bar"><span class="price">$47.58</span><span class="add-cart"><svg width="14" height="12" viewBox="0 0 16 14" aria-hidden="true"><path d="M1 1h2.5l2 8h8l1.5-6H4.2" fill="none" stroke="#9aa0a8" stroke-width="1.4"/><circle cx="6.5" cy="12" r="1.2" fill="#9aa0a8"/><circle cx="12.5" cy="12" r="1.2" fill="#9aa0a8"/></svg></span></div></article>
  <article class="product"><div class="product-media" role="img" aria-label="Photo of a remote control" style="background:linear-gradient(135deg,#eceef1,#26282c)"></div><h4>Product Name</h4><p>Short item description goes right here</p><div class="price-bar"><span class="price">$47.58</span><span class="add-cart"><svg width="14" height="12" viewBox="0 0 16 14" aria-hidden="true"><path d="M1 1h2.5l2 8h8l1.5-6H4.2" fill="none" stroke="#9aa0a8" stroke-width="1.4"/><circle cx="6.5" cy="12" r="1.2" fill="#9aa0a8"/><circle cx="12.5" cy="12" r="1.2" fill="#9aa0a8"/></svg></span></div></article>
  <article class="product"><div class="product-media" role="img" aria-label="Photo of a hair dryer" style="background:linear-gradient(135deg,#eceef1,#1e2024)"></div><h4>Product Name</h4><p>Short item description goes right here</p><div class="price-bar"><span class="price">$47.58</span><span class="add-cart"><svg width="14" height="12" viewBox="0 0 16 14" aria-hidden="true"><path d="M1 1h2.5l2 8h8l1.5-6H4.2" fill="none" stroke="#9aa0a8" stroke-width="1.4"/><circle cx="6.5" cy="12" r="1.2" fill="#9aa0a8"/><circle cx="12.5" cy="12" r="1.2" fill="#9aa0a8"/></svg></span></div></article>
  <article class="product"><div class="product-media" role="img" aria-label="Photo of a pair of speakers" style="background:linear-gradient(135deg,#eceef1,#121316)"></div><h4>Product Name</h4><p>Short item description goes right here</p><div class="price-bar"><span class="price">$47.58</span><span class="add-cart"><svg width="14" height="12" viewBox="0 0 16 14" aria-hidden="true"><path d="M1 1h2.5l2 8h8l1.5-6H4.2" fill="none" stroke="#9aa0a8" stroke-width="1.4"/><circle cx="6.5" cy="12" r="1.2" fill="#9aa0a8"/><circle cx="12.5" cy="12" r="1.2" fill="#9aa0a8"/></svg></span></div></article>
</section>

<h2 class="wrap section-title accent best-title">BEST SELLINGS</h2>
<section class="wrap grid best-grid">
  <article class="product"><div class="product-media" role="img" aria-label="Photo of a USB flash drive" style="background:linear-gradient(135deg,#eef0f2,#4e8f3a)"></div><h4>Product Name</h4><p>Short item description goes right here</p><div class="price-bar"><span class="price">$47.58</span><span class="add-cart"><svg width="14" height="12" viewBox="0 0 16 14" aria-hidden="true"><path d="M1 1h2.5l2 8h8l1.5-6H4.2" fill="none" stroke="#9aa0a8" stroke-width="1.4"/><circle cx="6.5" cy="12" r="1.2" fill="#9aa0a8"/><circle cx="12.5" cy="12" r="1.2" fill="#9aa0a8"/></svg></span></div></article>
  <article class="product"><div class="product-media" role="img" aria-label="Photo of a dash camera" style="background:linear-gradient(135deg,#eef0f2,#2a2c30)"></div><h4>Product Name</h4><p>Short item description goes right here</p><div class="price-bar"><span class="price">$47.58</span><span class="add-cart"><svg width="14" height="12" viewBox="0 0 16 14" aria-hidden="true"><path d="M1 1h2.5l2 8h8l1.5-6H4.2" fill="none" stroke="#9aa0a8" stroke-width="1.4"/><circle cx="6.5" cy="12" r="1.2" fill="#9aa0a8"/><circle cx="12.5" cy="12" r="1.2" fill="#9aa0a8"/></svg></span></div></article>
  <article class="product"><div class="product-media" role="img" aria-label="Photo of a handheld camcorder" style="background:linear-gradient(135deg,#eef0f2,#33363b)"></div><h4>Product Name</h4><p>Short item description goes right here</p><div class="price-bar"><span class="price">$47.58</span><span class="add-cart"><svg width="14" height="12" viewBox="0 0 16 14" aria-hidden="true"><path d="M1 1h2.5l2 8h8l1.5-6H4.2" fill="none" stroke="#9aa0a8" stroke-width="1.4"/><circle cx="6.5" cy="12" r="1.2" fill="#9aa0a8"/><circle cx="12.5" cy="12" r="1.2" fill="#9aa0a8"/></svg></span></div></article>
  <article class="product"><div class="product-media" role="img" aria-label="Photo of a game controller" style="background:linear-gradient(135deg,#eef0f2,#17181b)"></div><h4>Product Name</h4><p>Short item description goes right here</p><div class="price-bar"><span class="price">$47.58</span><span class="add-cart"><svg width="14" height="12" viewBox="0 0 16 14" aria-hidden="true"><path d="M1 1h2.5l2 8h8l1.5-6H4.2" fill="none" stroke="#9aa0a8" stroke-width="1.4"/><circle cx="6.5" cy="12" r="1.2" fill="#9aa0a8"/><circle cx="12.5" cy="12" r="1.2" fill="#9aa0a8"/></svg></span></div></article>
</section>

<footer class="site-footer">
  <div class="footer-cols">
    <div class="footer-col newsletter">
      <h5>NEWSLETTER SIGN UP</h5>
      <p>Get our latest offers and news</p>
      <div class="news-input"></div>
      <span class="btn-subscribe">SUBSCRIBE</span>
      <div class="pay-row"><i></i><i></i><i></i><i></i></div>
    </div>
    <div class="footer-col link-col">
      <h5>COMPANY</h5>
      <ul><li>About Us</li><li>Product Overview</li><li>Terms of Use</li><li>Order Now</li></ul>
    </div>
    <div class="footer-col link-col">
      <h5>PRODUCTS</h5>
      <ul><li>New Arrivals</li><li>Best Sellers</li><li>Special Offers</li><li>Gift Cards</li></ul>
    </div>
    <div class="footer-col link-col">
      <h5>SUPPORT</h5>
      <ul><li>FAQs</li><li>Privacy Policy</li><li>Returns</li><li>Contact</li></ul>
    </div>
    <div class="footer-col link-col">
      <h5>RESOURCES</h5>
      <ul><li>Store Locator</li><li>Trade Program</li><li>Careers</li><li>Press Room</li></ul>
    </div>
  </div>
  <div class="footer-bar">
    <div class="copyright">© 2024 Kenvo Electronics. All rights reserved.</div>
    <div class="social"><i></i><i></i><i></i><i></i></div>
  </div>
</footer>

</body>
</html>
```